Lightweight, clean Wordpress theme for fitness app website

Fit-Sprocket.com needs a new website.

Fit-Sprocket itself is a mobile fitness app and this website will support it and help to promote it with screenshots and descriptions of the app.

Attached is the logo. The main colours are the blue and white on the logo.

I need a fully functioning Wordpress theme for this website.

It needs to be clean, lightweight, fast loading and easy to maintain and build.
The theme should include the home page, pages and posts so that we can have the flexibility to do what we want.

It should work just as well on mobile as for desktop.

The target audience is all fitness lovers, female and male, any age.

Must Have:
- Wordpress theme.
- Pages, posts and a home page.
- Simple, clean & lightweight.
- Desktop & mobile styling
- See attachment for colours and fonts

Should Not Have:
- Bloated & slow loading designs

Target Market(s)

Fitness enthusiasts of all abilities.
Male / Female. Young & Old.
Should NOT use imagery of big body builders.

Industry/Entity Type

Fitness

Coding

Coded - Design and coding required

Number of Pages Required

3 page

Requirements
Must have
• Wordpress theme
• Landing / home page.
• Template for a page and a post.
• Simple, clean & fast loading.

```html
<!DOCTYPE html>
<html lang="en">
<head>
<meta charset="utf-8">
<title>Fit-Sprocket – Mobile Fitness App</title>
<link rel="stylesheet" href="https://fonts.googleapis.com/css2?family=Montserrat:wght@300;400;600;700&family=Open+Sans:wght@400;600&display=swap">
<style>
:root{
  --blue:#1c7fc3;
  --blue-band:#3a8fd0;
  --blue-button:#1a7cc3;
  --ink:#333333;
  --text:#5c5c5c;
  --white:#ffffff;
  --hero-dark:#1b1a1c;
  --contact-bg:#ececec;
  --field-border:#c9c9c9;
  --footer-bg:#262626;
  --footer-text:#d8d8d8;
  --footer-line:#3c3c3c;
}
*{box-sizing:border-box;margin:0;padding:0}
html,body{width:1200px;height:2908px;overflow:hidden}
body{position:relative;font-family:"Open Sans",Arial,sans-serif;color:var(--text);background:var(--white)}
.abs{position:absolute}

/* Hero */
.hero{left:0;top:0;width:1200px;height:654px;background:radial-gradient(ellipse at 55% 40%,#4a3a34 0%,#2a2526 45%,var(--hero-dark) 100%);overflow:hidden}
.hero-photo{left:0;top:0;width:1200px;height:654px;background:linear-gradient(90deg,rgba(20,20,22,.6) 0%,rgba(90,70,60,.25) 45%,rgba(60,60,64,.3) 70%,rgba(20,20,22,.6) 100%)}
.brand{left:88px;top:28px;width:120px;text-align:center;color:var(--white);font-family:"Montserrat",sans-serif;font-weight:600;font-size:15px}
.brand-mark{display:block;width:40px;height:40px;border-radius:50%;background:var(--white);margin:0 auto 10px}
.nav{left:472px;top:48px;display:flex;align-items:center;gap:0;font-family:"Montserrat",sans-serif;font-size:15px;color:var(--white)}
.nav a{color:var(--white);text-decoration:none;margin-right:46px}
.nav a.active{border-bottom:1px solid var(--white);padding-bottom:4px}
.nav .login{border:1.5px solid var(--white);border-radius:18px;padding:6px 18px;margin-right:0}
.hero-title{left:0;top:262px;width:1200px;text-align:center;color:var(--white);font-family:"Montserrat",sans-serif;font-weight:300;font-size:68px;letter-spacing:1px}
.hero-sub{left:0;top:346px;width:1200px;text-align:center;color:var(--white);font-family:"Montserrat",sans-serif;font-weight:600;font-size:26px}
.slide-arrow{top:314px;width:24px;height:24px}

/* About */
.about-photo{left:83px;top:675px;width:283px;height:467px;background:linear-gradient(180deg,#f4f1ef 0%,#d9cfc8 55%,#6f6a68 100%)}
.section-heading{font-family:"Montserrat",sans-serif;font-weight:700;color:var(--blue);font-size:34px;letter-spacing:1px}
.about-heading{left:458px;top:792px}
.body-copy{font-size:14.2px;line-height:25px;text-align:justify;color:var(--text)}
.about-copy{left:458px;top:845px;width:644px}
.read-more{left:458px;top:1023px;width:101px;height:33px;border:1.5px solid var(--blue);border-radius:17px;color:var(--blue);font-size:11px;display:flex;align-items:center;justify-content:center;font-family:"Montserrat",sans-serif}

/* Blog */
.blog{left:0;top:1142px;width:1200px;height:520px;background:var(--blue-band)}
.blog-heading{left:0;top:1214px;width:1200px;text-align:center;color:var(--white)}
.card{top:1293px;width:311px;height:287px;background:var(--white)}
.card-image{width:311px;height:185px}
.card-title{margin-top:16px;text-align:center;font-family:"Open Sans",sans-serif;font-size:18px;color:var(--ink)}
.card-text{margin:6px auto 0;width:220px;text-align:center;font-size:13px;line-height:20px;color:var(--text)}

/* App */
.app-photo{left:107px;top:1732px;width:333px;height:488px;background:linear-gradient(180deg,#ffffff 0%,#efe6e0 40%,#d8b8a6 100%)}
.app-heading{left:504px;top:1804px}
.app-copy{left:512px;top:1853px;width:552px}
.store-badge{top:2003px;height:43px;border-radius:6px;background:#111111}

/* Contact */
.contact{left:0;top:2216px;width:1200px;height:378px;background:var(--contact-bg)}
.contact-heading{left:0;top:2280px;width:1200px;text-align:center}
.field{height:58px;background:var(--white);border:1.5px solid var(--field-border);border-radius:3px;padding:0 12px;display:flex;align-items:center;font-size:15px;color:var(--ink)}
.submit{left:770px;top:2445px;width:285px;height:58px;background:var(--blue-button);color:var(--white);font-family:"Montserrat",sans-serif;font-size:19px;display:flex;align-items:center;justify-content:center;border-radius:2px}

/* Footer */
.footer{left:0;top:2594px;width:1200px;height:314px;background:var(--footer-bg)}
.footer-brand{left:104px;top:2650px;width:130px;text-align:center;color:var(--white);font-family:"Montserrat",sans-serif;font-weight:600;font-size:14px}
.social{top:2762px;width:21px;height:21px;background:var(--white);border-radius:3px}
.footer-heading{top:2652px;color:var(--white);font-family:"Montserrat",sans-serif;font-size:15px}
.footer-list{list-style:none;color:var(--footer-text);font-size:12.5px}
.contact-list li{display:flex;align-items:flex-start;gap:14px;margin-bottom:14px;line-height:21px}
.contact-list svg{flex:none;margin-top:4px}
.links-list li{margin-bottom:8px}
.links-list li::before{content:"» ";color:var(--white)}
.mail-copy{left:905px;top:2688px;width:210px;color:var(--footer-text);font-size:12px;line-height:18px}
.mail-form{left:905px;top:2733px;display:flex}
.mail-input{width:148px;height:29px;background:var(--white);font-size:11px;color:#888;display:flex;align-items:center;padding-left:8px}
.mail-submit{width:56px;height:29px;background:var(--blue-button);color:var(--white);font-size:12px;display:flex;align-items:center;justify-content:center}
.footer-rule{left:104px;top:2840px;width:992px;height:1px;background:var(--footer-line)}
.copyright{left:0;top:2860px;width:1200px;text-align:center;color:var(--white);font-size:12px}
</style>
</head>
<body>

<header class="abs hero">
  <div class="abs hero-photo" role="img" aria-label="Smiling man in gym gloves giving a thumbs up while holding a smartphone"></div>
  <div class="abs brand"><span class="brand-mark"></span>Fit-Sprocket.com</div>
  <nav class="abs nav">
    <a class="active">HOME</a><a>ABOUT US</a><a>BLOG</a><a>THE APP</a><a>CONTACT US</a><a class="login">LOGIN</a>
  </nav>
  <h1 class="abs hero-title">FIT-SPROCKET</h1>
  <p class="abs hero-sub">MOBILE FITNESS APP</p>
  <svg class="abs slide-arrow" style="left:69px" viewBox="0 0 24 24" aria-label="Previous slide"><circle cx="12" cy="12" r="11" fill="#111"/><path d="M14 7l-5 5 5 5" stroke="#fff" stroke-width="2" fill="none"/></svg>
  <svg class="abs slide-arrow" style="left:1101px" viewBox="0 0 24 24" aria-label="Next slide"><circle cx="12" cy="12" r="11" fill="#111"/><path d="M10 7l5 5-5 5" stroke="#fff" stroke-width="2" fill="none"/></svg>
</header>

<section class="about">
  <div class="abs about-photo" role="img" aria-label="Young woman in sportswear with earphones smiling at her phone"></div>
  <h2 class="abs section-heading about-heading">ABOUT US</h2>
  <p class="abs body-copy about-copy">It is a long established fact that a reader will be distracted by the readable content of a page when looking at its layout. The point of using Lorem Ipsum is that it has a more-or-less normal distribution of letters, as opposed to using 'Content here, content here', making it look like readable English. Many desktop publishing packages and web page editors now use Lorem Ipsum as their default model text, and a search for 'lorem ipsum' will uncover many web sites still in their infancy. Various versions have evolved over the years, sometimes by accident, sometimes on purpose.</p>
  <div class="abs read-more">READ MORE »</div>
</section>

<section class="abs blog" role="img" aria-label="Blue band with a faint photo of a phone and sneakers"></section>
<h2 class="abs section-heading blog-heading">LATEST BLOG</h2>
<article class="abs card" style="left:114px">
  <div class="card-image" role="img" aria-label="Group stretching in a fitness class" style="background:linear-gradient(135deg,#c9743a,#e8c9a8 60%,#6b5a4e)"></div>
  <h3 class="card-title">Neque porro quisquam</h3>
  <p class="card-text">It is a long established fact that a reader will be distracted</p>
</article>
<article class="abs card" style="left:444px">
  <div class="card-image" role="img" aria-label="Dumbbells, sneakers and a phone on the floor" style="background:linear-gradient(135deg,#5a5d62,#8d8f92 50%,#c9d04a)"></div>
  <h3 class="card-title">Quisquam est qui dolorem</h3>
  <p class="card-text">It is a long established fact that a reader will be distracted</p>
</article>
<article class="abs card" style="left:774px">
  <div class="card-image" role="img" aria-label="Woman jogging across a bridge at sunset" style="background:linear-gradient(135deg,#f3e9d8,#c8b7a0 50%,#8a8278)"></div>
  <h3 class="card-title">ipsum quia dolor</h3>
  <p class="card-text">It is a long established fact that a reader will be distracted</p>
</article>

<section class="app">
  <div class="abs app-photo" role="img" aria-label="Hand holding a smartphone showing the app calendar screen"></div>
  <h2 class="abs section-heading app-heading">THE APP</h2>
  <p class="abs body-copy app-copy">It is a long established fact that a reader will be distracted by the readable content of a page when looking at its layout. The point of using Lorem Ipsum is that it has a more-or-less normal distribution of letters, as opposed to using 'Content here, content here', making it look like readable English. Many desktop publishing packages and web page editors now use Lorem Ipsum as their default model text .</p>
  <div class="abs store-badge" style="left:512px;width:145px" role="img" aria-label="App store download badge"></div>
  <div class="abs store-badge" style="left:671px;width:142px" role="img" aria-label="App store download badge"></div>
</section>

<section class="abs contact"></section>
<h2 class="abs section-heading contact-heading">CONTACT US</h2>
<div class="abs field" style="left:165px;top:2370px;width:285px">NAME</div>
<div class="abs field" style="left:469px;top:2370px;width:285px">Email</div>
<div class="abs field" style="left:770px;top:2370px;width:285px">SUBJECT</div>
<div class="abs field" style="left:165px;top:2445px;width:589px">MESSAGE</div>
<div class="abs submit">SUBMIT</div>

<footer class="abs footer"></footer>
<div class="abs footer-brand"><span class="brand-mark" style="width:34px;height:34px"></span>Fit-Sprocket.com</div>
<span class="abs social" style="left:108px"></span>
<span class="abs social" style="left:141px"></span>
<span class="abs social" style="left:174px"></span>
<span class="abs social" style="left:207px"></span>

<h4 class="abs footer-heading" style="left:366px">CONTACT US</h4>
<ul class="abs footer-list contact-list" style="left:366px;top:2688px;width:230px">
  <li><svg width="12" height="15" viewBox="0 0 12 15"><path d="M6 0a6 6 0 0 0-6 6c0 4 6 9 6 9s6-5 6-9a6 6 0 0 0-6-6zm0 8.5a2.5 2.5 0 1 1 0-5 2.5 2.5 0 0 1 0 5z" fill="#fff"/></svg><span>2450 Harbor Lane North, Suite 210 Portland, OR 97209</span></li>
  <li><svg width="12" height="12" viewBox="0 0 12 12"><path d="M2.5 0l2 3-1.3 1.3a7 7 0 0 0 4.5 4.5L9 7.5l3 2-1.5 2.5C5 12 0 7 0 1.5z" fill="#fff"/></svg><span>503.555.0147</span></li>
  <li><svg width="13" height="10" viewBox="0 0 13 10"><rect width="13" height="10" rx="1" fill="#fff"/><path d="M0 1l6.5 5L13 1" stroke="#262626" stroke-width="1.3" fill="none"/></svg><span>hello@fit-sprocket.com</span></li>
</ul>

<h4 class="abs footer-heading" style="left:696px">QUICK LINKS</h4>
<ul class="abs footer-list links-list" style="left:700px;top:2690px">
  <li>The Bootcamp</li><li>Photo Gallery</li><li>The Gym</li><li>About us</li>
</ul>

<h4 class="abs footer-heading" style="left:905px">JOIN OUR MAILING LIST</h4>
<p class="abs mail-copy">Your about us information would fit here nicely.</p>
<div class="abs mail-form"><span class="mail-input">Email address</span><span class="mail-submit">Submit</span></div>

<div class="abs footer-rule"></div>
<p class="abs copyright">Copyright © 2017. All Rights Reserved</p>

</body>
</html>
```